【仕様】
・B5(182×257㎜)
・背幅は9㎜です(修正有)
・本文は横書きですので左綴じとなります。
・カバー(表1、表4、背表紙):4C(フルカラー)
・表紙(表1、表4、背表紙):1C
・扉:1C
・袖は10㎜
・帯のようなデザインは問題ありませんが、帯そのものをつける予定はありません。

※表紙・扉のデザインはカバーデザインに基づいたもので、「書名」「編者名」「社名(ロゴマーク)」だけが入っているもので結構です。
【デザインについて】
・書籍の内容は堅いですが、保育士をめざす学生がこの書籍を使って学びたくなるような、そして親しみをもてるデザインを希望します。

・イラスト等を加えていただいても結構です。

・書名等に用いる書体の指定はございません。

・書名、編者名等のデザインに盛り込む内容(文字)は添付ファイルを参照してください。
シンプル 複雑
単色 カラフル
暗い 明るい
日常 高級
遊び心 厳粛
未来的 伝統的
女性的 男性的
特に指定はありません。
• イラストレーター形式 (.ai)
【仕様】の項目で、袖の長さを10㎜と表記しておりましたが、110㎜に訂正いたします。

①学生が好みそうな非常にかわいらしく、やわらかいイメージ。
②「会話」の「 」の部分の葉っぱのデザイン。
③「保育内容」とコピー文の部分の色がカラフルで、きれいなデザイン。
④テキストという堅さをやわらげてくれるデザイン。

この度は多くのご提案をありがとうございました。
それぞれに様々な思いを込めて作成いただいたことを、とてもうれしく感じました。感謝申し上げます。
今回採用できなかった提案の中にも、他の書籍のカバーとして採用したいと思うものが多くありました。
今後も様々な書籍で依頼をさせていただく予定でおりますので、また是非ご応募いただき、皆さんのお力をお借りしながら、一つの書籍という作品を世に送り出せればと考えておりますので、どうぞよろしくお願い申し上げます。

```html
<!DOCTYPE html>
<html lang="ja">
<head>
<meta charset="utf-8">
<title>保育をまなぶ人の領域テキスト「会話」</title>
<link rel="stylesheet" href="https://fonts.googleapis.com/css2?family=M+PLUS+Rounded+1c:wght@400;500;700&display=swap">
<style>
  :root {
    --paper: #fbf8ef;
    --title-orange: #ec9a4c;
    --leaf-green: #5ea233;
    --ink-gray: #6b6b6b;
    --ink-dark: #4a4a4a;
    --band-yellow: #f6e29c;
    --step-gray: #a7a7a7;
    --drop-blue-light: #dbeef6;
    --drop-blue: #b9dcec;
    --sprout-light: #e6f1c6;
    --sprout-green: #a9cf4d;
    --note-white: #fffdf4;
  }
  html, body {
    margin: 0;
    padding: 0;
    overflow: hidden;
  }
  body {
    width: 820px;
    height: 1200px;
    font-family: "M PLUS Rounded 1c", sans-serif;
  }
  .cover {
    position: relative;
    width: 820px;
    height: 1200px;
    background: var(--paper);
    overflow: hidden;
  }
  .rain-art {
    position: absolute;
    left: 380px;
    top: 110px;
    width: 420px;
    height: 520px;
    border-radius: 40px;
    background: radial-gradient(ellipse at 60% 40%, var(--drop-blue) 0%, var(--drop-blue-light) 55%, rgba(219,238,246,0) 80%);
  }
  .lower-band {
    position: absolute;
    left: 0;
    top: 790px;
    width: 820px;
    height: 410px;
    background: var(--band-yellow);
  }
  .sprout-art {
    position: absolute;
    left: 190px;
    top: 590px;
    width: 630px;
    height: 290px;
    border-radius: 140px 140px 0 0;
    background: radial-gradient(ellipse at 50% 45%, var(--sprout-green) 0%, var(--sprout-light) 60%, rgba(230,241,198,0) 85%);
  }
  .series-title {
    position: absolute;
    left: 46px;
    top: 26px;
    margin: 0;
    color: var(--title-orange);
    font-weight: 400;
    font-size: 62px;
    line-height: 80px;
    letter-spacing: 14px;
  }
  .book-title {
    position: absolute;
    left: 30px;
    top: 190px;
    margin: 0;
    color: var(--leaf-green);
    font-weight: 500;
    font-size: 118px;
    line-height: 1.1;
    letter-spacing: 0;
  }
  .editor {
    position: absolute;
    left: 60px;
    top: 400px;
    margin: 0;
    color: var(--ink-gray);
    font-size: 22px;
    letter-spacing: 4px;
  }
  .steps {
    position: absolute;
    left: 48px;
    top: 884px;
    display: flex;
    align-items: center;
    gap: 6px;
  }
  .step {
    background: var(--step-gray);
    color: #fff;
    font-size: 20px;
    padding: 2px 12px;
    letter-spacing: 1px;
  }
  .step-arrow {
    width: 14px;
    height: 14px;
  }
  .steps-caption {
    position: absolute;
    left: 48px;
    top: 930px;
    margin: 0;
    color: var(--ink-dark);
    font-size: 26px;
    font-weight: 500;
    letter-spacing: 4px;
  }
  .appendix {
    position: absolute;
    left: 40px;
    top: 990px;
    width: 560px;
    height: 190px;
    background: var(--note-white);
    box-sizing: border-box;
    padding: 14px 20px;
    color: var(--ink-dark);
  }
  .appendix-lead {
    margin: 0 0 8px;
    font-size: 25px;
    font-weight: 500;
    letter-spacing: 3px;
  }
  .appendix-list {
    margin: 0;
    padding: 0;
    list-style: none;
    font-size: 18px;
    line-height: 30px;
  }
  .appendix-list li::before {
    content: "●";
    font-size: 12px;
    margin-right: 8px;
    vertical-align: 2px;
  }
  .publisher {
    position: absolute;
    left: 680px;
    top: 1124px;
    display: flex;
    align-items: center;
    gap: 8px;
    color: var(--ink-dark);
    font-size: 24px;
    font-weight: 500;
  }
  .publisher-dot {
    width: 32px;
    height: 32px;
    border-radius: 50%;
    background: var(--drop-blue);
  }
</style>
</head>
<body>
  <main class="cover">
    <div class="rain-art" role="img" aria-label="やわらかな水色の雨つぶが降ってくるイラスト"></div>
    <div class="lower-band"></div>
    <div class="sprout-art" role="img" aria-label="黄緑色の双葉の芽が伸びるイラスト"></div>

    <h2 class="series-title">保育をまなぶ人の<br>領域テキスト</h2>
    <h1 class="book-title">「会話」</h1>
    <p class="editor">森田 由紀子 編</p>

    <div class="steps">
      <span class="step">基礎編</span>
      <svg class="step-arrow" viewBox="0 0 10 10"><polygon points="1,0 9,5 1,10" fill="#a7a7a7"/></svg>
      <span class="step">実践編</span>
      <svg class="step-arrow" viewBox="0 0 10 10"><polygon points="1,0 9,5 1,10" fill="#a7a7a7"/></svg>
      <span class="step">実技編</span>
      <svg class="step-arrow" viewBox="0 0 10 10"><polygon points="1,0 9,5 1,10" fill="#a7a7a7"/></svg>
      <span class="step">発展編</span>
    </div>
    <p class="steps-caption">4編構成でステップアップ学習！</p>

    <section class="appendix">
      <p class="appendix-lead">学びをより深めるため巻末に付録！</p>
      <ul class="appendix-list">
        <li>心・身体・言葉の発達表</li>
        <li>主な園行事の紹介</li>
        <li>パペットを制作してみよう</li>
        <li>幼稚園教育要領（抄）・保育所保育指針（抄）</li>
      </ul>
    </section>

    <div class="publisher">
      <span class="publisher-dot"></span>
      <span class="publisher-name">あさひ</span>
    </div>
  </main>
</body>
</html>
```